Tarvel Business Card Design

We need a business card design for a new company in NJ called Tarvel LLC. We provide plumbing, sewer & drain cleaning, and full bath remodeling services. We need a logo design that will be used for several applications such as; cards, stickers, t shirts, and truck lettering. The company hopes to one day be a full service operation offering plumbing, heating, cooling, electric, so we need a design that is very general (aka no pipe wrenches). Colors will be royal blue,neon lime green, and would like to add diamond plate or steel plate to give it a very masculine feel and look.

Contact Information for Business Card

Tarvel LLC. ,Plumbing, Sewer & Drain Cleaning, Bath Remodeling
North Brunswick, NJ 08902
732.555.0148
Tarvelpipeworks.example
Info@tarvelpipeworks.example
Stay calm, ring tarvel!, Rick Movren- President
NJ Master Plumbing License: 58217, Residential & Commercial Service

Requirements
Should not have
• Tool icons
Script font

```html
<!DOCTYPE html>
<html lang="en">
<head>
<meta charset="utf-8">
<title>Tarvel LLC Business Card</title>
<link href="https://fonts.googleapis.com/css2?family=Lato:wght@400;700&display=swap" rel="stylesheet">
<style>
  :root {
    --stage: #2b2b2d;
    --card-black: #111113;
    --card-white: #f4f4f6;
    --royal-blue: #2a3893;
    --lime: #5cbf4f;
    --steel: #b9bcc2;
    --steel-dark: #6a6d73;
    --ink-blue: #2f3a8f;
  }
  * { box-sizing: border-box; margin: 0; padding: 0; }
  html, body { width: 1200px; height: 750px; overflow: hidden; }
  body {
    background: var(--stage);
    font-family: "Lato", sans-serif;
    position: relative;
  }
  .card {
    position: absolute;
    top: 220px;
    width: 540px;
    height: 309px;
    overflow: hidden;
    box-shadow: 0 10px 30px rgba(0,0,0,.45);
  }
  .card-back { left: 40px; background: var(--card-black); }
  .card-front { left: 620px; background: var(--card-white); }

  /* back side */
  .plate-texture {
    position: absolute; inset: 0;
    background: radial-gradient(ellipse at 60% 40%, #26272b 0%, #151618 55%, #0c0c0e 100%);
  }
  .back-brand {
    position: absolute; left: 118px; top: 92px;
    display: flex; align-items: center; gap: 14px;
  }
  .back-brand .dot {
    width: 60px; height: 60px; border-radius: 50%;
    border: 5px solid var(--steel);
  }
  .back-brand .name {
    font-weight: 700; font-size: 46px; letter-spacing: 6px;
    color: var(--steel);
  }
  .back-services {
    position: absolute; left: 0; right: 0; top: 196px;
    text-align: center; font-variant: small-caps;
    font-size: 17px; letter-spacing: .5px; color: var(--steel);
  }
  .back-tagline {
    position: absolute; left: 0; right: 0; top: 236px;
    text-align: center; font-variant: small-caps;
    font-size: 20px; letter-spacing: 1.5px; color: var(--steel-dark);
  }

  /* front side */
  .front-brand {
    position: absolute; left: 40px; top: 118px;
    display: flex; flex-direction: column; align-items: center; gap: 10px;
    width: 210px;
  }
  .front-brand .dot {
    width: 74px; height: 74px; border-radius: 50%;
    border: 6px solid var(--lime);
  }
  .front-brand .name {
    font-weight: 700; font-size: 40px; letter-spacing: 4px;
    color: var(--royal-blue);
  }
  .contact {
    position: absolute; left: 292px; top: 38px; width: 240px;
    color: var(--ink-blue);
  }
  .contact .person { font-size: 22px; font-weight: 700; }
  .contact .role { font-size: 14px; color: var(--lime); margin-bottom: 12px; }
  .contact .row {
    display: flex; align-items: center; gap: 7px;
    font-size: 12.5px; margin-bottom: 5px;
  }
  .contact .row.phone { font-size: 17px; margin-top: 6px; }
  .contact .row svg { width: 13px; height: 13px; flex: none; }
  .contact .license {
    margin-top: 14px; font-size: 12px; line-height: 1.35;
  }
  .divider {
    position: absolute; left: 282px; top: 130px; width: 1px; height: 70px;
    background: #c9cbd2;
  }
  .front-bands { position: absolute; left: 0; bottom: 0; width: 540px; height: 120px; }
</style>
</head>
<body>

<section class="card card-back" aria-label="Card back">
  <div class="plate-texture" role="img" aria-label="Gloss black steel plate texture with repeating brand mark pattern"></div>
  <div class="back-brand">
    <span class="dot"></span>
    <span class="name">TARVEL</span>
  </div>
  <p class="back-services">Plumbing | Sewer &amp; Drain Cleaning | Bath Remodeling</p>
  <p class="back-tagline">Stay calm, ring tarvel!</p>
</section>

<section class="card card-front" aria-label="Card front">
  <div class="front-brand">
    <span class="dot"></span>
    <span class="name">TARVEL</span>
  </div>

  <div class="divider"></div>

  <div class="contact">
    <p class="person">Rick Movren</p>
    <p class="role">President</p>
    <p class="row">
      <svg viewBox="0 0 12 12"><path d="M6 0.5a4 4 0 0 1 4 4c0 3-4 7-4 7s-4-4-4-7a4 4 0 0 1 4-4z" fill="var(--lime)"/><circle cx="6" cy="4.5" r="1.5" fill="#fff"/></svg>
      Wexbury Falls NJ 08731
    </p>
    <p class="row phone">
      <svg viewBox="0 0 12 12"><rect width="12" height="12" rx="2" fill="var(--lime)"/><path d="M3.5 2.8l1.3-.3.8 2-1 .7a5 5 0 0 0 2.2 2.2l.7-1 2 .8-.3 1.3C6.5 9 3 5.5 3.5 2.8z" fill="#fff"/></svg>
      732.555.0148
    </p>
    <p class="row">
      <svg viewBox="0 0 12 12"><rect y="2" width="12" height="8" rx="1" fill="var(--lime)"/><path d="M1 3l5 4 5-4" stroke="#fff" fill="none"/></svg>
      Info@tarvelpipeworks.example
    </p>
    <p class="row">
      <svg viewBox="0 0 12 12"><circle cx="6" cy="6" r="5.5" fill="var(--lime)"/><path d="M.5 6h11M6 .5c-2.5 3-2.5 8 0 11M6 .5c2.5 3 2.5 8 0 11" stroke="#fff" stroke-width=".8" fill="none"/></svg>
      www.tarvelpipeworks.example
    </p>
    <p class="license">NJ Master Plumbing License: 58217<br>Residential &amp; Commercial Service</p>
  </div>

  <svg class="front-bands" viewBox="0 0 540 120" preserveAspectRatio="none">
    <polygon points="300,60 540,60 540,120 280,120" fill="var(--lime)"/>
    <polygon points="0,98 290,98 282,120 0,120" fill="var(--royal-blue)"/>
    <polygon points="150,70 300,70 290,98 140,98" fill="var(--royal-blue)" opacity=".8"/>
  </svg>
</section>

</body>
</html>
```